PowerPoint Presentation

We are looking for a new PPT layout template existing of a cover page, three internal pages - one with text bullets, one with a picture/information and one with more of a table for pricing information and the last a last "thank you - contact info" page. Feel free to grab any graphics from our website at www.larkhavenmetrics.com

Any product can be chosen from our products page. Colors are cyan and orange and feel free to choose darker backgrounds for the front and end page. Also included in the graphics is our new business card design.

Also note we are updating our website, and have attached a sample of how it looks for reference.

Reason: We are still looking for submissions for our PowerPoint presentation. We have increased the award amount as well.

Target Market(s)

Target market is private industry professionals, public safety organizations, and state and local government agencies.

Industry/Entity Type

Business

Colors
33a6d7
86cae6
cee9f5
f68d4d
f8ba93
fce2d4

```html
<!DOCTYPE html>
<html lang="en">
<head>
<meta charset="utf-8">
<title>Larkhaven Metrics – Presentation Template</title>
<link rel="stylesheet" href="https://fonts.googleapis.com/css2?family=Arimo:wght@400;700&family=Open+Sans:wght@400;600&display=swap">
<style>
:root{
  --page:#e9e6e1;
  --navy:#265a82;
  --navy-bar:#1f5475;
  --black:#111111;
  --orange:#f08a24;
  --orange-light:#fbc35a;
  --yellow:#f5e61a;
  --cream:#f3e79a;
  --table-orange:#eb7a2a;
  --text-blue:#1f5475;
  --slide-light:#ffffff;
  --slide-shade:#e6e6e6;
  --mark-grey:#7a7a7a;
  --white:#ffffff;
}
*{box-sizing:border-box;margin:0;padding:0}
html,body{width:1080px;height:1200px;overflow:hidden}
body{background:var(--page);position:relative;font-family:"Open Sans",Arial,sans-serif}
.slide{position:absolute;width:492px;height:368px;overflow:hidden;box-shadow:0 3px 10px rgba(0,0,0,.25)}
.slide--cover{left:30px;top:22px}
.slide--areas{left:558px;top:22px}
.slide--prices{left:30px;top:414px}
.slide--product{left:558px;top:414px}
.slide--thanks{left:294px;top:808px}

/* dark cover and closing slides */
.dark{background:var(--navy)}
.brand-band{position:absolute;left:0;top:0;width:100%;height:54px;background:linear-gradient(to bottom,var(--orange-light),var(--orange));display:flex;align-items:center;justify-content:center}
.brand-name{font-family:Arimo,Arial,sans-serif;font-weight:700;font-size:21px;color:var(--black);letter-spacing:.5px}
.top-rule{position:absolute;left:0;top:54px;width:100%;height:9px;background:var(--black)}
.foot{position:absolute;left:0;bottom:0;width:100%;height:28px;background:var(--black);border-top:3px solid var(--white);display:flex;align-items:center;justify-content:space-between;padding:0 10px;font-family:Arimo,Arial,sans-serif;font-size:11px;color:var(--yellow)}
.foot .presenter{font-weight:700}
.cover-title{position:absolute;left:0;width:100%;top:152px;text-align:center;font-family:Arimo,Arial,sans-serif;font-weight:700;font-size:27px;color:var(--yellow)}
.cover-subtitle{position:absolute;left:0;width:100%;top:208px;text-align:center;font-size:21px;color:var(--cream)}

/* light internal slides */
.light{background:radial-gradient(ellipse at 50% 40%,var(--slide-light) 30%,var(--slide-shade) 100%)}
.title-rule{position:absolute;top:20px;height:3px;width:100%;left:0;background:var(--navy-bar)}
.title-bar{position:absolute;left:10px;top:6px;width:472px;height:30px;background:var(--navy-bar);color:var(--white);font-family:Arimo,Arial,sans-serif;font-weight:400;font-size:19px;text-align:center;line-height:30px}
.footer-mark{position:absolute;left:10px;bottom:14px;display:flex;align-items:center;gap:6px;font-family:Arimo,Arial,sans-serif;font-weight:700;font-size:12px;color:var(--mark-grey);letter-spacing:.3px}
.footer-mark .mark-dot{width:10px;height:10px;border-radius:50%;background:#33a6d7}
.footer-rule{position:absolute;left:190px;right:0;bottom:20px;height:4px;background:var(--black)}
.page-num{position:absolute;right:14px;bottom:8px;width:28px;height:28px;border-radius:50%;background:var(--black);color:var(--orange);font-family:Arimo,Arial,sans-serif;font-weight:700;font-size:15px;text-align:center;line-height:28px}

/* service areas */
.areas{position:absolute;top:95px;list-style:none}
.areas--left{left:72px}
.areas--right{left:306px}
.areas li{display:flex;align-items:center;gap:10px;height:30px;font-size:13px;color:#333}
.areas svg{width:10px;height:14px}

/* price table */
.price-table{position:absolute;left:32px;top:64px;width:428px;border-collapse:collapse;font-size:9px}
.price-table th{background:var(--table-orange);color:var(--white);font-weight:400;height:22px;font-size:10px}
.price-table td{border:2px solid var(--table-orange);height:53px;color:var(--text-blue);font-weight:600;padding-left:8px;white-space:nowrap}
.price-table .col-img{width:118px;text-align:center;padding:0}
.price-table .col-name{width:193px}
.thumb{display:inline-block;width:56px;height:36px;border-radius:3px;background:linear-gradient(#f4f4f4,#9a9a9a)}
.thumb--dark{background:linear-gradient(#6b6b6b,#222)}

/* product */
.product-photo{position:absolute;left:42px;top:106px;width:168px;height:150px;border-radius:6px;background:radial-gradient(ellipse at 50% 40%,#f2f2f2,#8d8d8d)}
.product-name{position:absolute;left:246px;top:150px;font-size:11px;font-weight:600;color:var(--table-orange)}
.product-desc{position:absolute;left:246px;top:184px;width:210px;font-size:9px;line-height:12px;color:var(--text-blue)}

/* thank you */
.thanks-title{position:absolute;left:0;width:100%;top:114px;text-align:center;font-family:Arimo,Arial,sans-serif;font-weight:700;font-size:27px;color:var(--yellow)}
.contact-label{position:absolute;left:72px;top:176px;font-size:18px;color:var(--yellow)}
.contact-list{position:absolute;left:172px;top:204px;list-style:none;font-family:Arimo,Arial,sans-serif;font-size:9.5px;line-height:12px;color:#dfe6ee}
.contact-list b{color:var(--white)}
</style>
</head>
<body>

<section class="slide slide--cover dark">
  <div class="brand-band"><span class="brand-name">LARKHAVEN METRICS</span></div>
  <div class="top-rule"></div>
  <h1 class="cover-title">PRESENTATION TITLE</h1>
  <p class="cover-subtitle">Presentation Subtitle</p>
  <div class="foot"><span>03 March 2014</span><span class="presenter">PRESENTOR'S NAME</span><span>Job Title</span></div>
</section>

<section class="slide slide--areas light">
  <div class="title-rule"></div>
  <h2 class="title-bar">SERVICE AREAS</h2>
  <ul class="areas areas--left">
    <li><svg viewBox="0 0 10 14"><path d="M5 0a5 5 0 0 0-5 5c0 4 5 9 5 9s5-5 5-9a5 5 0 0 0-5-5zm0 7a2 2 0 1 1 0-4 2 2 0 0 1 0 4z" fill="#1f5475"/></svg>Africa</li>
    <li><svg viewBox="0 0 10 14"><path d="M5 0a5 5 0 0 0-5 5c0 4 5 9 5 9s5-5 5-9a5 5 0 0 0-5-5zm0 7a2 2 0 1 1 0-4 2 2 0 0 1 0 4z" fill="#1f5475"/></svg>America - U.S.</li>
    <li><svg viewBox="0 0 10 14"><path d="M5 0a5 5 0 0 0-5 5c0 4 5 9 5 9s5-5 5-9a5 5 0 0 0-5-5zm0 7a2 2 0 1 1 0-4 2 2 0 0 1 0 4z" fill="#1f5475"/></svg>Asia</li>
    <li><svg viewBox="0 0 10 14"><path d="M5 0a5 5 0 0 0-5 5c0 4 5 9 5 9s5-5 5-9a5 5 0 0 0-5-5zm0 7a2 2 0 1 1 0-4 2 2 0 0 1 0 4z" fill="#1f5475"/></svg>Australia - South Pacific</li>
    <li><svg viewBox="0 0 10 14"><path d="M5 0a5 5 0 0 0-5 5c0 4 5 9 5 9s5-5 5-9a5 5 0 0 0-5-5zm0 7a2 2 0 1 1 0-4 2 2 0 0 1 0 4z" fill="#1f5475"/></svg>Canada</li>
  </ul>
  <ul class="areas areas--right">
    <li><svg viewBox="0 0 10 14"><path d="M5 0a5 5 0 0 0-5 5c0 4 5 9 5 9s5-5 5-9a5 5 0 0 0-5-5zm0 7a2 2 0 1 1 0-4 2 2 0 0 1 0 4z" fill="#1f5475"/></svg>Carribean</li>
    <li><svg viewBox="0 0 10 14"><path d="M5 0a5 5 0 0 0-5 5c0 4 5 9 5 9s5-5 5-9a5 5 0 0 0-5-5zm0 7a2 2 0 1 1 0-4 2 2 0 0 1 0 4z" fill="#1f5475"/></svg>Central America</li>
    <li><svg viewBox="0 0 10 14"><path d="M5 0a5 5 0 0 0-5 5c0 4 5 9 5 9s5-5 5-9a5 5 0 0 0-5-5zm0 7a2 2 0 1 1 0-4 2 2 0 0 1 0 4z" fill="#1f5475"/></svg>Europe</li>
    <li><svg viewBox="0 0 10 14"><path d="M5 0a5 5 0 0 0-5 5c0 4 5 9 5 9s5-5 5-9a5 5 0 0 0-5-5zm0 7a2 2 0 1 1 0-4 2 2 0 0 1 0 4z" fill="#1f5475"/></svg>Middle East</li>
    <li><svg viewBox="0 0 10 14"><path d="M5 0a5 5 0 0 0-5 5c0 4 5 9 5 9s5-5 5-9a5 5 0 0 0-5-5zm0 7a2 2 0 1 1 0-4 2 2 0 0 1 0 4z" fill="#1f5475"/></svg>South America</li>
  </ul>
  <div class="footer-mark"><span class="mark-dot"></span>LARKHAVENMETRICS</div>
  <div class="footer-rule"></div>
  <div class="page-num">01</div>
</section>

<section class="slide slide--prices light">
  <div class="title-rule"></div>
  <h2 class="title-bar">PRODUCTS &amp; PRICES</h2>
  <table class="price-table">
    <thead><tr><th>PRODUCTS</th><th>PRODUCT NAMES</th><th>PRICES</th></tr></thead>
    <tbody>
      <tr><td class="col-img"><span class="thumb" role="img" aria-label="Product photo: fixed satellite dish"></span></td><td class="col-name">Fixed Satellite Systems &amp; Service Plans</td><td>$000</td></tr>
      <tr><td class="col-img"><span class="thumb" role="img" aria-label="Product photo: satellite terminal"></span></td><td class="col-name">Kestrel Terminal</td><td>$000</td></tr>
      <tr><td class="col-img"><span class="thumb" role="img" aria-label="Product photo: motorized satellite dish"></span></td><td class="col-name">Fixed Motorized Satellite Dish</td><td>$000</td></tr>
      <tr><td class="col-img"><span class="thumb thumb--dark" role="img" aria-label="Product photo: rack controller unit"></span></td><td class="col-name">FIELDCORE Controller</td><td>$000</td></tr>
    </tbody>
  </table>
  <div class="footer-mark"><span class="mark-dot"></span>LARKHAVENMETRICS</div>
  <div class="footer-rule"></div>
  <div class="page-num">02</div>
</section>

<section class="slide slide--product light">
  <div class="title-rule"></div>
  <h2 class="title-bar">PRODUCTS</h2>
  <div class="product-photo" role="img" aria-label="Product photo: VSAT satellite dish on a weighted mount"></div>
  <h3 class="product-name">Fixed Satellite Systems &amp; Service Plans</h3>
  <p class="product-desc">Performance grade VSAT satellite dishes and NexaLink service capable of providing speeds of 5Mbps down and 2Mbps up</p>
  <div class="footer-mark"><span class="mark-dot"></span>LARKHAVENMETRICS</div>
  <div class="footer-rule"></div>
  <div class="page-num">03</div>
</section>

<section class="slide slide--thanks dark">
  <div class="brand-band"><span class="brand-name">LARKHAVEN METRICS</span></div>
  <div class="top-rule"></div>
  <h2 class="thanks-title">THANK YOU!</h2>
  <p class="contact-label">Contact us:</p>
  <ul class="contact-list">
    <li><b>Sales - USA - Canada - International</b></li>
    <li>Monday - Friday 8 a.m. to 5 p.m. Pacific Standard Time</li>
    <li>Monday - Friday 11 a.m. to 8 p.m. Eastern Standard Time</li>
    <li>Tel: <b>800-555-0142</b> (Toll Free USA Only)</li>
    <li>Tel: <b>805-555-0190</b> (USA, Canada)</li>
    <li>Tel: <b>+1-805-555-0190</b> (International)</li>
    <li>Fax: <b>805-555-0173</b></li>
    <li>General Sales Email - <b>sales@larkhavenmetrics.com</b></li>
  </ul>
  <div class="foot"><span>03 March 2014</span><span class="presenter">PRESENTOR'S NAME</span><span>Job Title</span></div>
</section>

</body>
</html>
```